Fun but professional website required for school teaching consultancy.

Dear Designers,

I have an interesting brief for you. My client is a skilled teacher who is looking to promote her consultancy that provides bespoke training and support to other teachers.

She would like a website that promotes her philosophy for working with children, which is essentially that she wants to create a fun and creative learning environment for them, whilst maintaining the professionalism that is also required to succeed. Representation of the balance between these two points is crucial to the design.

Typically these kind of websites are pretty boring so we need something fun and vibrant, not uninviting ie those typical images of a teacher sat behind a desk or anything overly formal.

Here is an example of what we do not want: http://www.brightmarrowlearning.co.uk/ - in this one although my client liked the layout, she hated the graphics.

Here is a website that she really liked and captured the vibe of what she is trying to promote about herself: http://www.pellowfieldkidsplace.com/ - this design indicates fun with learning, happy kids, lively colours and still has a professional feel as well.

If you have any further questions, please ask

Many thanks,

Garth

PS Enclosed please find a whole bunch of resources (including site map) for this project. My client has supplied graphics, page content and plenty of visuals so hopefully this will make things easier
Updates

To all designers,

Thanks all your designs. Just to let you all know they have been sent to the client and I will supply feedback to you all individually when I get it.

Many thanks,
Garth

Hi all,

We've had loads of designs for this project so thanks to you all very much. If there is any feedback to pass on, I will do this directly. Right now, all designs have been liked and are in the running. My client is going through them all and will make a decision on the deadline date which is the 10th May.
If you don't hear from me before then, it's simply because no alterations have been requested.

Many thanks.
Garth

Industry/Entity Type

Training

```html
<!DOCTYPE html>
<html lang="en">
<head>
<meta charset="utf-8">
<title>Brightpath Consultancy Ltd</title>
<link href="https://fonts.googleapis.com/css2?family=Open+Sans:ital,wght@0,400;0,600;0,700;1,400&family=Noto+Serif:ital@0;1&display=swap" rel="stylesheet">
<style>
:root{
  --sky:#0a97e0;
  --sky-dark:#0b86c6;
  --ink:#222;
  --body:#555;
  --muted:#aaa;
  --rule:#e6e6e6;
  --green:#6bb52b;
  --green-dark:#4f9a14;
  --night:#000;
  --foot-text:#fff;
}
*{margin:0;padding:0;box-sizing:border-box}
html,body{width:1051px;height:1200px;overflow:hidden;background:var(--night)}
body{font-family:"Open Sans",Arial,sans-serif;color:var(--body)}
.stage{position:relative;width:1200px;height:1370px;transform:scale(.87583);transform-origin:0 0;background:var(--night)}
.sky-band{position:absolute;left:0;top:0;width:1200px;height:908px;background:var(--sky)}
.page{position:absolute;left:120px;top:0;width:981px;height:1091px;background:#fff;border-bottom:3px solid var(--sky-dark)}
.abs{position:absolute}
.brand-mark{left:150px;top:30px;width:50px;height:50px;border-radius:50%;background:var(--sky)}
.brand-name{left:219px;top:38px;font-size:25px;color:var(--ink);line-height:1}
.brand-sub{left:220px;top:67px;font-size:14px;color:var(--ink);letter-spacing:.3px}
.search{left:800px;top:19px;width:278px;height:32px;display:flex}
.search-field{flex:1;border:1px solid #ddd;border-right:0;font-size:11px;color:#bbb;padding:9px 12px}
.search-btn{width:80px;background:linear-gradient(#6dbb2c,#55a116);color:#fff;font-size:12px;text-align:center;line-height:32px}
.nav{right:121px;top:73px;font-size:13.5px;color:#555;display:flex;gap:10px}
.nav span.sep{color:#777}
.hero{left:140px;top:118px;width:940px;height:312px;background:linear-gradient(100deg,#7c8a5a 0%,#c9c0b2 25%,#556b2a 48%,#8e5a4a 60%,#c7d1d6 80%,#3d4a22 100%)}
.sec-icon{width:32px;height:32px;border-radius:50%;background:var(--sky);display:flex;align-items:center;justify-content:center}
.sec-title{font-size:16px;color:var(--ink)}
.media{background:linear-gradient(#6e6552,#8e8a7a 45%,#b7a08a 75%,#5d5a4c)}
.video{left:140px;top:516px;width:310px;height:166px}
.play{left:273px;top:580px;width:44px;height:44px;border-radius:50%;background:rgba(255,255,255,.55)}
.intro{left:141px;top:699px;width:312px;font-size:11.4px;line-height:16px}
.intro b{color:#333;font-weight:700}
.dots{left:271px;top:779px;display:flex;gap:6px}
.dots i{width:6px;height:6px;border-radius:50%;background:#ddd;display:block}
.dots i.on{background:var(--sky)}
.news{left:470px;width:311px;height:108px;border-bottom:1px solid var(--rule)}
.news .thumb{position:absolute;left:2px;top:0;width:60px;height:58px;background:linear-gradient(#4c5b2a,#c29f85 60%,#6d4a3c)}
.news h3{position:absolute;left:78px;top:-2px;font-family:"Noto Serif",Georgia,serif;font-weight:400;font-size:14px;color:var(--sky)}
.news .date{position:absolute;left:78px;top:18px;font-family:"Noto Serif",Georgia,serif;font-style:italic;font-size:10.5px;color:var(--muted)}
.news p{position:absolute;left:78px;top:40px;width:230px;font-size:11.5px;line-height:16px}
.download{left:799px;top:457px;width:280px;height:67px;background:linear-gradient(#76c232,#57a618);border-bottom:2px solid var(--green-dark)}
.download small{position:absolute;left:59px;top:13px;font-size:12px;color:#fff}
.download strong{position:absolute;left:58px;top:27px;font-family:"Noto Serif",Georgia,serif;font-weight:400;font-size:19px;color:#fff}
.testi-head{left:799px;top:550px;width:281px;height:35px;background:#f2f2f2;border-top:1px solid var(--sky);font-family:"Noto Serif",Georgia,serif;font-size:13.5px;color:var(--ink);padding:8px 14px}
.quote{left:814px;top:598px;font-family:"Noto Serif",Georgia,serif;font-size:34px;color:#666;line-height:1}
.testi-text{left:849px;top:602px;width:225px;font-size:11.5px;line-height:18px}
.testi-text p{margin-bottom:14px}
.testi-name{left:850px;top:778px;font-size:12px;font-weight:700;color:#333}
.testi-name span{color:var(--muted);font-weight:600}
.testi-rule{left:799px;top:819px;width:281px;height:1px;background:var(--rule)}
.gallery-rule{left:140px;top:897px;width:940px;height:1px;background:var(--rule)}
.shot{top:931px;height:109px}
.arrow{width:18px;height:18px;border-radius:50%;background:#666;display:flex;align-items:center;justify-content:center}
.foot-h{top:1132px;font-size:17px;color:var(--foot-text);font-weight:400}
.foot-list{font-size:12px;color:var(--foot-text);list-style:none}
.foot-list li{height:28px;padding-left:21px;position:relative}
.foot-list li::before{content:"→";position:absolute;left:0;top:-1px;font-size:10px}
.contact{left:621px;top:1164px;font-size:12px;color:var(--foot-text);line-height:27px}
.social{left:861px;top:1163px;font-size:12px;color:var(--foot-text)}
.social div{display:flex;align-items:center;gap:12px;height:31px}
.social i{width:24px;height:24px;border-radius:50%;background:#ccc;display:block}
.foot-rule{left:140px;top:1310px;width:940px;height:1px;background:#333}
.copy{left:140px;top:1331px;font-size:11px;font-style:italic;color:var(--foot-text)}
</style>
</head>
<body>
<div class="stage">
  <div class="sky-band"></div>
  <div class="page"></div>

  <div class="abs brand-mark"></div>
  <div class="abs brand-name">Brightpath</div>
  <div class="abs brand-sub">Consultancy Ltd</div>

  <div class="abs search"><div class="search-field">Type your keywords...</div><div class="search-btn">Search</div></div>
  <nav class="abs nav"><span>Home</span><span class="sep">|</span><span>Services</span><span class="sep">|</span><span>What people say</span><span class="sep">|</span><span>Founder Profile</span><span class="sep">|</span><span>Contact us</span></nav>

  <div class="abs hero" role="img" aria-label="Three children looking closely at a large green leaf outdoors"></div>

  <div class="abs sec-icon" style="left:140px;top:463px"><svg width="12" height="12" viewBox="0 0 12 12"><rect x="1" y="1" width="10" height="10" fill="none" stroke="#fff" stroke-width="1.6"/><line x1="4" y1="1" x2="4" y2="11" stroke="#fff"/><line x1="8" y1="1" x2="8" y2="11" stroke="#fff"/></svg></div>
  <div class="abs sec-title" style="left:183px;top:469px">Children’s Activities</div>
  <div class="abs media video" role="img" aria-label="Video still of children hanging upside down on a climbing frame"></div>
  <div class="abs play"></div>
  <svg class="abs" style="left:289px;top:591px" width="16" height="22" viewBox="0 0 16 22"><path d="M0 0L16 11L0 22Z" fill="#fff"/></svg>
  <p class="abs intro"><b>Morbi leo risus</b>, porta ac consectetur ac, vestibulum at estibulum id ligula porta felis euismod semper.Nulla vite libero, a pharetra augue. Donec ullamcorper nulla nonu s auctor fringilla.</p>
  <div class="abs dots"><i></i><i></i><i class="on"></i><i></i></div>

  <div class="abs sec-icon" style="left:469px;top:463px"><svg width="12" height="12" viewBox="0 0 12 12"><path d="M1 4H4L8 1V11L4 8H1Z" fill="#fff"/></svg></div>
  <div class="abs sec-title" style="left:511px;top:469px">What’s New</div>

  <article class="abs news" style="top:515px;height:89px"><div class="thumb" role="img" aria-label="Boy outdoors"></div><h3>Aenean Lorem Fringilla</h3><div class="date">Posted on 12 Jul 2012</div><p>Lorem ipsum dolor sit amet, consectetur adipiscing elit. e dapibus, tellus ac.</p></article>
  <article class="abs news" style="top:621px;height:90px"><div class="thumb" role="img" aria-label="Boy in a checked shirt"></div><h3>Condimentum Fusce Venenatis</h3><div class="date">Posted on 12 Jul 2012</div><p>Lorem ipsum dolor sit amet, consectetur adipiscing elit. e dapibus, tellus ac.</p></article>
  <article class="abs news" style="top:730px;height:89px"><div class="thumb" role="img" aria-label="Girl outdoors"></div><h3>Ipsum Justo Commodo</h3><div class="date">Posted on 12 Jul 2012</div><p>Lorem ipsum dolor sit amet, consectetur adipiscing elit. e dapibus, tellus ac.</p></article>

  <div class="abs download">
    <svg style="position:absolute;left:23px;top:22px" width="24" height="24" viewBox="0 0 24 24" fill="none" stroke="#fff" stroke-width="2"><rect x="2" y="4" width="20" height="18"/><line x1="7" y1="1" x2="7" y2="6"/><line x1="17" y1="1" x2="17" y2="6"/><path d="M7 11h2M11 11h2M15 11h2M7 15h2M11 15h2M15 15h2M7 19h2M11 19h2" stroke-width="2"/></svg>
    <small>Download</small><strong>Application</strong>
  </div>
  <div class="abs testi-head">Student Testimonial</div>
  <div class="abs quote">“</div>
  <div class="abs testi-text">
    <p>Nulla vitae elit libero, a pharetra augue. ipsum dolor sit amet, consectetur adipisi elit. Aenean lacinia bibendum nulla sed consectetur nibh elit. Lorem ipsum dolor amet, consectetur adipiscing elit.</p>
    <p>Nulla vitae elit libero, a pharetra augue. ipsum dolor sit amet, consectetur adipisi elit. Aenean lacinia bibendum</p>
  </div>
  <div class="abs testi-name">John Doe, <span>5 years old</span></div>
  <div class="abs testi-rule"></div>

  <div class="abs sec-icon" style="left:140px;top:841px"><svg width="12" height="12" viewBox="0 0 12 12"><path d="M6 0.5L7.6 4.2L11.5 4.5L8.5 7L9.4 11L6 8.9L2.6 11L3.5 7L0.5 4.5L4.4 4.2Z" fill="#fff"/></svg></div>
  <div class="abs sec-title" style="left:182px;top:848px">Photo Gallery</div>
  <div class="abs gallery-rule"></div>

  <div class="abs arrow" style="left:166px;top:977px"><svg width="8" height="8" viewBox="0 0 8 8"><path d="M5.5 1L2.5 4L5.5 7" fill="none" stroke="#fff" stroke-width="1.6"/></svg></div>
  <div class="abs media shot" style="left:217px;width:136px" role="img" aria-label="Child hanging upside down on a climbing frame"></div>
  <div class="abs media shot" style="left:383px;width:136px" role="img" aria-label="Children playing on a climbing frame"></div>
  <div class="abs media shot" style="left:550px;width:136px" role="img" aria-label="Girl hanging from a climbing net"></div>
  <div class="abs media shot" style="left:714px;width:135px" role="img" aria-label="Child upside down by a wooden fence"></div>
  <div class="abs media shot" style="left:874px;width:133px;top:934px;height:107px" role="img" aria-label="Child hanging on a climbing net"></div>
  <div class="abs arrow" style="left:1039px;top:979px"><svg width="8" height="8" viewBox="0 0 8 8"><path d="M2.5 1L5.5 4L2.5 7" fill="none" stroke="#fff" stroke-width="1.6"/></svg></div>

  <h2 class="abs foot-h" style="left:140px">Pharetra Quam Adipiscing</h2>
  <ul class="abs foot-list" style="left:140px;top:1170px"><li>STEP Start</li><li>STEP Gym</li><li>STEP Athletics</li><li>STEP Games</li></ul>
  <ul class="abs foot-list" style="left:380px;top:1170px"><li>STEP Dance</li><li>STEP OAA</li></ul>

  <h2 class="abs foot-h" style="left:621px">Contact Us</h2>
  <div class="abs contact">Telephone:<br>07700 900418<br>Email:<br>hello@brightpathconsult.co.uk</div>

  <h2 class="abs foot-h" style="left:861px">Follow Us</h2>
  <div class="abs social">
    <div><i></i>Circle Share</div>
    <div><i></i>Bloglet</div>
    <div><i></i>Work Links</div>
    <div><i></i>Chirper</div>
  </div>

  <div class="abs foot-rule"></div>
  <div class="abs copy">Copy right 2014. All right reserved.</div>
</div>
</body>
</html>
```